CD/Album cover design - Ember & Tide

Hi, I need an album cover designed. The name of the album is called 'Ember and Tide' Not 100% sure of the concept, but using colored lines, Geometrical shapes etc, angles and maybe a circle or triangle in the middle. A cross between, Velvet Harbor ,Hollow rim of the sea (But dont make it look like this old look album) , 80s retro synthwave album covers, perhaps with neon color lines but not all of it etc. Have it modern looking . My name on cover and album name. Back, songs etc and info details. The style of the music is EDM meets guitar. Trap, house music and guitar as the main theme instrument, with sythns. Keep it relatively simple looking, and maybe have the background white,, but with the color designs, wording etc colors. or if you feel it would look better another way, just use your own judgement and creativity. Ve attached a couple of Pics. The Velvet Harbor pic , more of concept. The retro one... I like the design in the middle but not wording at the top. The QX rise one, I like how the wording is in the middle of circle. So a combination of these, with geometrical lines, colors, etc. I am also open to a completely new idea that you think would look awesome. The album is really combining Guitar with House/Tap EDM music, and the concept Ember and Tide - The beginning and end (Of everything) Thanks
EDM , Guitarists
Music, EDM, Guitar Instrumental

```html
<!DOCTYPE html>
<html lang="en">
<head>
<meta charset="utf-8">
<title>Rune Calder — Ember &amp; Tide</title>
<link href="https://fonts.googleapis.com/css2?family=Mr+Dafoe&family=Jost:wght@100;200&display=swap" rel="stylesheet">
<style>
  :root {
    --orange: #ff8a00;
    --flame: #ff2a0a;
    --red: #e8102a;
    --magenta: #f2004e;
    --pink: #f06a78;
    --teal: #1f5a5a;
    --slate: #2a2a38;
    --black: #020204;
    --white: #ffffff;
    --glow: rgba(255, 255, 255, 0.75);
  }
  html, body {
    margin: 0;
    padding: 0;
    width: 1200px;
    height: 1200px;
    overflow: hidden;
    background: var(--black);
  }
  .album-cover {
    position: relative;
    width: 1200px;
    height: 1200px;
    overflow: hidden;
    background:
      radial-gradient(ellipse 520px 380px at 610px 380px, rgba(255, 34, 8, 0.95), transparent 70%),
      radial-gradient(ellipse 420px 360px at 1050px 470px, rgba(242, 0, 78, 0.95), transparent 72%),
      radial-gradient(ellipse 380px 300px at 120px 40px, rgba(255, 146, 0, 0.95), transparent 75%),
      radial-gradient(ellipse 300px 260px at 1120px 60px, rgba(240, 110, 120, 0.9), transparent 75%),
      radial-gradient(ellipse 260px 220px at 20px 500px, rgba(31, 90, 90, 0.9), transparent 75%),
      radial-gradient(ellipse 340px 220px at 1100px 850px, rgba(42, 42, 56, 0.9), transparent 75%),
      linear-gradient(160deg, var(--orange) 0%, var(--flame) 28%, var(--red) 42%, #5a1020 58%, var(--black) 74%, var(--black) 100%);
  }
  .artist-name {
    position: absolute;
    top: 108px;
    left: 0;
    width: 1200px;
    margin: 0;
    text-align: center;
    font-family: "Mr Dafoe", cursive;
    font-weight: 400;
    font-size: 190px;
    line-height: 1;
    color: var(--white);
    transform: translateX(10px) skewX(-4deg);
    text-shadow: 0 0 8px var(--glow), 0 0 22px rgba(255, 255, 255, 0.45);
  }
  .album-title {
    position: absolute;
    top: 505px;
    left: 0;
    width: 1200px;
    margin: 0;
    text-align: center;
    font-family: "Jost", sans-serif;
    font-weight: 100;
    font-size: 166px;
    line-height: 236px;
    letter-spacing: 4px;
    color: var(--white);
    text-shadow: 0 0 6px var(--glow), 0 0 16px rgba(255, 255, 255, 0.35);
  }
  .album-title span { display: block; }
</style>
</head>
<body>
  <main class="album-cover">
    <h2 class="artist-name">Rune Calder</h2>
    <h1 class="album-title">
      <span class="title-line">EMBER &amp;</span>
      <span class="title-line">TIDE</span>
    </h1>
  </main>
</body>
</html>
```